Hot Pilates studio needs window graphics/ front signage

We need window graphics for the front of our hot pilates studio. We have several large front windows that are visible from the street and would be beneficial to have signage. Glow Loft offers several different heated classes on the mat including: Hot Pilates, Sculpt, Hot Barre. I would like for people that drive by to know what we are. The window dimensions are (4 windows) 41 inches X 61 inches, (4 windows) 34 inches X 61 inches (a total of 8 window panels)

Target Market(s)

fit women and men ages 16-65

Industry/Entity Type

fitness, pilates,

Font styles to use
Sans Serif

Colors

Designer to choose only greyscale colors for use in the design.

Requirements
Must have
• HOT PILATES
Nice to have
• our hashtag is #KeepItBright

```html
<!DOCTYPE html>
<html lang="en">
<head>
<meta charset="utf-8">
<title>Glow Loft – Window Graphic</title>
<link href="https://fonts.googleapis.com/css2?family=League+Spartan:wght@600;700;800&family=Allura&display=swap" rel="stylesheet">
<style>
  :root {
    --backdrop: #000000;
    --panel: #aeaeae;
    --headline: #f8f8f8;
    --ink: #000000;
  }
  html, body {
    margin: 0;
    padding: 0;
    width: 1200px;
    height: 1200px;
    overflow: hidden;
    background: var(--backdrop);
  }
  .canvas {
    position: relative;
    width: 1200px;
    height: 1200px;
    background: var(--backdrop);
  }
  .window-panel {
    position: absolute;
    left: 68px;
    top: 361px;
    width: 1064px;
    height: 477px;
    background: var(--panel);
  }
  .headline {
    position: absolute;
    left: 0;
    right: 0;
    top: 140px;
    margin: 0;
    text-align: center;
    font-family: "League Spartan", sans-serif;
    font-weight: 800;
    font-size: 128px;
    line-height: 1;
    letter-spacing: -0.01em;
    color: var(--headline);
    text-transform: uppercase;
    white-space: nowrap;
  }
  .class-line {
    position: absolute;
    left: 0;
    right: 0;
    top: 262px;
    margin: 0;
    text-align: center;
    font-family: "League Spartan", sans-serif;
    font-weight: 700;
    font-size: 26px;
    line-height: 1;
    letter-spacing: 0.32em;
    text-indent: 0.32em;
    color: var(--headline);
    text-transform: uppercase;
  }
  .studio-name {
    position: absolute;
    left: 0;
    right: 0;
    top: 312px;
    margin: 0;
    text-align: center;
    font-family: "Allura", cursive;
    font-weight: 400;
    font-size: 58px;
    line-height: 1;
    color: var(--ink);
  }
  .hashtag-strip {
    position: absolute;
    left: 36px;
    right: 36px;
    bottom: 4px;
    display: flex;
    justify-content: space-between;
    margin: 0;
    padding: 0;
    list-style: none;
  }
  .hashtag {
    font-family: "League Spartan", sans-serif;
    font-weight: 700;
    font-size: 16px;
    letter-spacing: 0.06em;
    text-transform: uppercase;
    color: var(--ink);
    line-height: 1.4;
  }
</style>
</head>
<body>
  <main class="canvas">
    <section class="window-panel">
      <h1 class="headline">Sweat With Us</h1>
      <p class="class-line">Hot Pilates</p>
      <p class="studio-name">Glow Loft</p>
      <ul class="hashtag-strip">
        <li class="hashtag">#KeepItBright</li>
        <li class="hashtag">#KeepItBright</li>
        <li class="hashtag">#KeepItBright</li>
        <li class="hashtag">#KeepItBright</li>
        <li class="hashtag">#KeepItBright</li>
        <li class="hashtag">#KeepItBright</li>
        <li class="hashtag">#KeepItBright</li>
      </ul>
    </section>
  </main>
</body>
</html>
```